International Marketing Company - Web Design Project

kVesta is a well-funded start up in London developing an Online Marketing Platform for small businesses in Europe.

We require a large number of high quality business web designs for our business website builder. Our business websites are completely integrated into our Online Marketing systems and therefore it is important for designers to comply with our Design Guidelines.

This initial contest is a trial for us to open up the design process to top designers for the Builders vertical (e.g. Builders, Electricians, Plumbers, Flooring, etc.). We have implemented a base html structure and design and included them in the files.

Use your creativity to design new and fresh designs based on the included elements (e.g. testimonials, business description, etc).

We will award the stated prize money for the top three designs.

Any designers that submit designs we feel are of a high enough quality but do not make the top 3 could still be compensated and WILL be invited to participate in our next vertical competition.

Therefore, we encourage designers to submit as many designs as possible as we may award up to 25 designs.

Submissions will be reviewed daily and feedback provided where possible.

Designers who can also code will have the options to implement their designs for an additional fee.

Good luck!
Updates

There has been a mistake made in regard to the prize. Pixel Harbor should have it fixed soon.

1st place = £350
2nd place = £250
3rd Place = £150

Thanks,
Dorian
25/11/2011

UPDATE:

1st place will win £350
2nd place will win £250
3rd place will win £150

Everything else is as to the specification.

Thanks
Dorian

Target Market(s)

Builders, Electricians, Plumbers, Tradesman, Small construction companies

Industry/Entity Type

Business

Requirements
Must have
• Totally new designs based around the elements we want to show on each page.

We are looking for something different to the design we already have. But you can use that as a starting point.

Use the included files to see what is required for each page. Here is a brief outline:

Homepage - Testimonials, News, Business Description, Latest Projects and Call to action

About-Us - Team Summary, About the Business and a call to action

Projects Page - Project Details (Oage Title and description), Each project needs a title, content and 2 images.

Testimonials Page - The testifiers name and their comment

Contacts Page - Trovix Map, Company address, business hours, contact form and a call to action.

Please submit final designs in Photoshop or Fireworks format.

Each page has a set of elements. These element must feature in the design of that page. See supporting documents for page details.

All elements must be included in your design. Please do not add any extra element.

Professional look and feel
Nice to have
• Design variations:
Full width designs
Boxed Designs
With AND without carousels
OR static images
Good use of stock images.

Creative use of the elements, dont be restricted/influenced by the default design we have already

Designs based on the 960 grid

```html
<!DOCTYPE html>
<html lang="en">
<head>
<meta charset="utf-8">
<title>Kestrel Builders</title>
<link href="https://fonts.googleapis.com/css2?family=Arimo:wght@400;700&family=Questrial&family=Cinzel:wght@700&family=Lora:ital@1&display=swap" rel="stylesheet">
<style>
:root{
  --navy:#0b5a7e;
  --navy-dark:#084866;
  --footer:#0b4f6e;
  --footer-deep:#083d56;
  --touch:#1a6f96;
  --banner-a:#0a5c82;
  --banner-b:#1688b5;
  --strip:#dcdcdc;
  --text:#3a3a3a;
  --muted:#8a8a8a;
  --panel:#f1f1f1;
  --panel-head:#d6d6d6;
  --line:#d4d4d4;
  --white:#ffffff;
}
*{margin:0;padding:0;box-sizing:border-box}
html,body{width:943px;height:1200px;overflow:hidden;background:var(--white)}
body{position:relative;font-family:"Arimo",Arial,sans-serif;color:var(--text)}
.abs{position:absolute}

.top-rule{left:0;top:0;width:943px;height:4px;background:var(--navy)}
.header{left:0;top:4px;width:943px;height:78px;background:linear-gradient(#fff,#f0f3f5)}
.brand{left:60px;top:20px;font-family:"Questrial",sans-serif;font-size:38px;letter-spacing:3px;color:var(--navy)}
.callus{right:46px;top:30px;display:flex;align-items:center;gap:10px;font-family:"Questrial",sans-serif;font-size:20px;color:#666}

.nav{left:0;top:82px;width:943px;height:31px;background:var(--navy);display:flex}
.nav a{color:#fff;text-decoration:none;font-family:"Questrial",sans-serif;font-size:17px;line-height:31px;padding:0 0 0 48px;width:auto}
.nav-item{position:absolute;top:0;height:31px;line-height:31px;color:#fff;font-family:"Questrial",sans-serif;font-size:17px}
.nav-sep{position:absolute;top:0;width:1px;height:31px;background:rgba(255,255,255,.25)}

.banner{left:0;top:113px;width:943px;height:297px;background:linear-gradient(90deg,var(--banner-a),var(--banner-b) 50%,var(--banner-a))}
.banner-photo{left:90px;top:122px;width:756px;height:278px;background:linear-gradient(160deg,#4a3a2a 0%,#a8835a 45%,#c9a06a 70%,#8d6b45 100%)}
.arrow{position:absolute}

.strip{left:0;top:410px;width:943px;height:40px;background:var(--strip);font-family:"Questrial",sans-serif;font-size:18px;color:#777;line-height:40px;padding-left:78px;letter-spacing:.3px}

.welcome{left:49px;top:473px;font-size:21px;font-weight:700;color:var(--navy)}
.about{left:52px;top:510px;width:575px;font-size:11px;line-height:19.5px;color:#444}
.about p{margin-bottom:19.5px}
.quote-box{left:96px;top:707px;width:473px;height:91px;border:1px solid #d8d8d8;border-radius:6px;background:#fff;box-shadow:0 1px 3px rgba(0,0,0,.08)}
.quote-mark{left:104px;top:713px;font-family:"Lora",serif;font-size:44px;color:#d0d0d0}
.quote-text{left:144px;top:727px;width:410px;font-family:"Lora",serif;font-style:italic;font-size:12.5px;line-height:21px;color:#9a9a9a}
.quote-name{left:399px;top:809px;font-size:11px;font-weight:700;color:#333}
.quote-nav{left:531px;top:806px;font-size:12px;color:#999;letter-spacing:6px}

.col-rule{left:644px;top:470px;width:1px;height:345px;background:var(--line)}
.quote-btn{left:655px;top:471px;width:236px;height:49px;background:var(--navy-dark);color:#fff;font-family:"Cinzel",serif;font-size:20px;line-height:49px;text-align:center;box-shadow:0 3px 5px rgba(0,0,0,.25)}
.news{left:655px;top:537px;width:239px;height:274px;background:var(--panel);box-shadow:0 3px 5px rgba(0,0,0,.18)}
.news-head{height:39px;background:var(--panel-head);font-size:17px;line-height:39px;padding-left:13px;color:#333}
.news-item{position:relative;margin:0 3px;height:50px;border-bottom:1px solid #dcdcdc;padding:8px 6px 0 33px;font-size:11px;line-height:18px;color:#555}
.news-item::before{content:"";position:absolute;left:13px;top:14px;border-left:4px solid #d7772c;border-top:3px solid transparent;border-bottom:3px solid transparent}
.news-more{position:absolute;right:24px;bottom:17px;font-size:10px;color:#888}

.projects-title{left:58px;top:830px;font-size:18px;font-weight:700;color:var(--navy)}
.projects{left:0;top:864px;width:943px;height:145px;background:linear-gradient(#f6f6f6,#fff)}
.thumb{position:absolute;top:881px;width:168px;height:83px;background:linear-gradient(135deg,#3d2d22,#b98a5e 55%,#e9d9c2);box-shadow:0 4px 6px rgba(0,0,0,.2)}
.caption{position:absolute;top:982px;width:168px;text-align:center;font-size:11px;color:#333}

.footer{left:0;top:1009px;width:943px;height:166px;background:var(--footer)}
.links{position:absolute;top:1032px;list-style:none;font-size:10.5px;color:#b8d3e0}
.links li{height:20.7px;line-height:20.7px;padding-left:11px;position:relative}
.links li::before{content:"";position:absolute;left:0;top:8px;border-left:3px solid #b8d3e0;border-top:2.5px solid transparent;border-bottom:2.5px solid transparent}
.touch{left:628px;top:1031px;width:271px;height:93px;background:var(--touch);border:1px solid #2d86ad}
.touch h2{position:absolute;left:0;width:100%;top:12px;text-align:center;font-family:"Questrial",sans-serif;font-weight:400;font-size:20px;color:#fff}
.email{position:absolute;left:13px;top:47px;width:208px;height:31px;background:var(--footer-deep);color:#c9dde7;font-size:12px;line-height:31px;padding-left:12px}
.go{position:absolute;left:221px;top:47px;width:37px;height:31px;background:var(--footer-deep);border-left:1px solid #3b7d9c;color:#fff;font-weight:700;font-size:15px;line-height:31px;text-align:center}
.follow{left:631px;top:1134px;font-family:"Questrial",sans-serif;font-size:21px;color:#9fb9c6}
.social{position:absolute;top:1134px;width:27px;height:27px;border-radius:5px;background:#8ea9b6}
.social.active{background:#3ea3d6}
.copyright{left:0;top:1175px;width:943px;height:25px;background:var(--footer-deep);font-size:10px;color:#6f93a5;line-height:25px;padding-left:46px}
</style>
</head>
<body>
<div class="abs top-rule"></div>
<header class="abs header"></header>
<div class="abs brand">Logo</div>
<div class="abs callus">
  <svg width="26" height="26" viewBox="0 0 26 26"><circle cx="13" cy="13" r="11.5" fill="none" stroke="#777" stroke-width="1.5"/><path d="M9 7c-1 1-1.5 2.5 0 5.5s4 5.5 6.5 6.5c1.5.5 2.5 0 3-1l-2.5-2.5-1.5 1c-1.5-.8-3-2.5-3.8-4l1-1.5z" fill="#777"/></svg>
  <span>Call us: 101 111 1111</span>
</div>

<nav class="abs nav" aria-label="Main">
  <span class="nav-item" style="left:48px">HOME</span>
  <span class="nav-sep" style="left:120px"></span>
  <span class="nav-item" style="left:139px">ABOUT US</span>
  <span class="nav-sep" style="left:233px"></span>
  <span class="nav-item" style="left:258px">TESTIMONIALS</span>
  <span class="nav-sep" style="left:384px"></span>
  <span class="nav-item" style="left:409px">PORTFOLIO</span>
  <span class="nav-sep" style="left:516px"></span>
  <span class="nav-item" style="left:541px">CONTACTS</span>
</nav>

<section class="abs banner"></section>
<div class="abs banner-photo" role="img" aria-label="Photo of a modern kitchen with wooden island and oak floor"></div>
<svg class="arrow" style="left:99px;top:248px" width="20" height="24" viewBox="0 0 20 24"><path d="M16 2 5 12l11 10" fill="none" stroke="#0b5a7e" stroke-width="5"/></svg>
<svg class="arrow" style="left:812px;top:248px" width="20" height="24" viewBox="0 0 20 24"><path d="M4 2l11 10L4 22" fill="none" stroke="rgba(255,255,255,.45)" stroke-width="5"/></svg>
<div class="abs strip">Lorem ipsum dolor sit amet, sectetuer adipiscing elit. Aenean commodo ligula eget dolor.</div>

<h1 class="abs welcome">WELCOME TO KESTREL BUILDERS</h1>
<div class="abs about">
  <p>I am an experienced builder in Crawley, Kestrel Construction have been based in Crawley for over 10 years. My team and I are proven, reliable builders based in Crawley. We've come across a lot in our time, so don't hesitate to get in touch about any building job in Crawley.</p>
  <p>I am a friendly, handyman who has built a team of excellent tradesmen based in Crawley. My builders in Crawley have years of experience in kitchen renovation, bathroom renovation, roofing and plumbing, loft conversions and house restoration.</p>
  <p>Call Kestrel Construction on 01 23456789 now to discuss how we can help you. My quotes are always FREE with no obligation.</p>
</div>
<div class="abs quote-box"></div>
<div class="abs quote-mark">&ldquo;</div>
<div class="abs quote-text">Kestrel Construction are the best builders in Crawley. They are experts in all areas of house building and I am extremely satisfied with my new loft conversion.</div>
<div class="abs quote-name">Mr. Halloway</div>
<div class="abs quote-nav">&lt; &gt;</div>

<div class="abs col-rule"></div>
<div class="abs quote-btn">Get a Quote Now</div>
<aside class="abs news">
  <div class="news-head">LATEST NEWS</div>
  <div class="news-item">Kestrel Construction have just finished another fine job in Crawley.</div>
  <div class="news-item">Kestrel Construction have just finished another fine job in Crawley.</div>
  <div class="news-item">Kestrel Construction have just finished another fine job in Crawley.</div>
  <div class="news-item">Kestrel Construction have just finished another fine job in Crawley.</div>
  <span class="news-more">More</span>
</aside>

<h2 class="abs projects-title">LATEST PROJECTS</h2>
<section class="abs projects"></section>
<svg class="arrow" style="left:52px;top:915px" width="20" height="24" viewBox="0 0 20 24"><path d="M16 2 5 12l11 10" fill="none" stroke="#0b5a7e" stroke-width="5"/></svg>
<svg class="arrow" style="left:875px;top:915px" width="20" height="24" viewBox="0 0 20 24"><path d="M4 2l11 10L4 22" fill="none" stroke="#cfcfcf" stroke-width="5"/></svg>
<div class="thumb" style="left:82px" role="img" aria-label="Photo of a restored room with wooden floor"></div>
<div class="thumb" style="left:287px" role="img" aria-label="Photo of a loft conversion bedroom"></div>
<div class="thumb" style="left:492px" role="img" aria-label="Photo of a loft conversion bedroom"></div>
<div class="thumb" style="left:697px" role="img" aria-label="Photo of a loft conversion bedroom"></div>
<div class="caption" style="left:82px">House restoration in Crawley</div>
<div class="caption" style="left:287px">House restoration in Crawley</div>
<div class="caption" style="left:492px">House restoration in Crawley</div>
<div class="caption" style="left:697px">House restoration in Crawley</div>

<footer class="abs footer"></footer>
<ul class="links" style="left:53px"><li>home</li><li>about us</li><li>testimonials</li><li>portfolio</li><li>contacts</li></ul>
<ul class="links" style="left:183px"><li>home</li><li>about us</li><li>testimonials</li><li>portfolio</li><li>contacts</li></ul>
<ul class="links" style="left:329px"><li>home</li><li>about us</li><li>testimonials</li><li>portfolio</li><li>contacts</li></ul>
<div class="abs touch">
  <h2>Get In Touch With Us</h2>
  <div class="email">Enter Your e - mail</div>
  <div class="go">GO</div>
</div>
<div class="abs follow">Follow us:</div>
<span class="social" style="left:742px"></span>
<span class="social active" style="left:773px"></span>
<span class="social" style="left:805px"></span>
<span class="social" style="left:836px"></span>
<span class="social" style="left:868px"></span>
<div class="abs copyright">&copy; Copyright 2011 Kestrel Builders. All Rights Reserved.</div>
</body>
</html>
```